Business Card Design needed Have Logo Files

Hello, I am in need of a business card design.

Company Name: Quartz Traders

Company Address:
2714 E. Palmer Ave
Suite 482B
North Las Vegas, Nevada 97415

I think the colors blue, grey, silver (metallic), white, and black are good choices to go with for coloring.

The Owen Pratt and the Copper Sheet are my favorites from the examples so far. Love the bring and edgy blues.

Photo's I have added are designs that I like. I'll also be adding source files.

Logo Source documents have been added.

Project Deadline Extended
Reason: Father passed away and had to take care of his affairs, back in business now.

Need front and back. Try to give it a backside that has a wow factor to it. I've changed the color spectrum to blue, black, purple, and pink for the front side. Think of it as 90% blue and black, 7% purple, 3 % pink when it comes to thinking of ratios of how much of each color i'd like to see on the card. Backside you can use any of those 4 colors as much as you'd like to give it memorable.

Industry/Entity Type

Business

Colors
0492cd
33a6d7
0355a3
3176b5
ffffff
aaaaaa
cbcbcb
9d9d9d
5c5c5c

Requirements
Must have
• Name
Company Address
Work Number
Mobile Number

Doublesided.
Rounded edges

```html
<!DOCTYPE html>
<html lang="en">
<head>
<meta charset="utf-8">
<title>Quartz Traders Business Card</title>
<link rel="stylesheet" href="https://fonts.googleapis.com/css2?family=Lato:wght@400;700;900&display=swap">
<style>
  :root {
    --page-bg: #e9e9ec;
    --card-black: #0a0a0c;
    --card-black-soft: #1c1c20;
    --blue-light: #6a86dc;
    --blue-deep: #3a50b8;
    --purple: #a34bc9;
    --pink: #f3b9cf;
    --logo-blue: #33a6d7;
    --logo-blue-light: #8fd4f2;
    --white: #ffffff;
  }
  html, body {
    margin: 0;
    padding: 0;
    width: 1200px;
    height: 1023px;
    overflow: hidden;
    background: var(--page-bg);
    font-family: "Lato", sans-serif;
  }
  .canvas {
    position: relative;
    width: 1200px;
    height: 1023px;
  }
  .card {
    position: absolute;
    left: 200px;
    width: 800px;
    height: 457px;
    border-radius: 40px;
    overflow: hidden;
    box-shadow: 0 14px 30px rgba(0,0,0,0.25);
  }
  .card--front { top: 40px; }
  .card--back {
    top: 530px;
    background: radial-gradient(ellipse at 40% 20%, var(--card-black-soft), var(--card-black) 70%);
  }
  .front-art {
    position: absolute;
    inset: 0;
    width: 100%;
    height: 100%;
  }
  .contact {
    position: absolute;
    top: 38px;
    right: 48px;
    text-align: right;
    color: var(--white);
  }
  .contact__name {
    margin: 0;
    font-size: 34px;
    font-weight: 900;
    color: var(--pink);
    letter-spacing: 0.5px;
  }
  .contact__title {
    margin: 2px 0 22px;
    font-size: 20px;
    font-weight: 400;
  }
  .contact__line {
    display: flex;
    justify-content: flex-end;
    align-items: center;
    gap: 10px;
    margin: 3px 0;
    font-size: 19px;
    line-height: 1.3;
  }
  .contact__line svg { width: 18px; height: 18px; flex: none; }
  .contact__spacer { width: 18px; flex: none; }
  .contact__address {
    margin-top: 16px;
    font-size: 19px;
    line-height: 1.35;
  }
  .brand {
    position: absolute;
    display: flex;
    align-items: center;
    gap: 18px;
  }
  .brand__dot {
    border-radius: 50%;
    background: var(--logo-blue-light);
    flex: none;
  }
  .brand__name {
    font-family: "Lato", sans-serif;
    font-weight: 900;
    color: var(--logo-blue);
    letter-spacing: 2px;
    text-transform: uppercase;
    line-height: 1.05;
  }
  .card--front .brand { left: 56px; bottom: 52px; gap: 16px; }
  .card--front .brand__dot { width: 50px; height: 50px; }
  .card--front .brand__name { font-size: 40px; }
  .card--back .brand {
    left: 50%;
    top: 50%;
    transform: translate(-50%, -50%);
  }
  .card--back .brand__dot { width: 76px; height: 76px; }
  .card--back .brand__name { font-size: 64px; }
</style>
</head>
<body>
<main class="canvas">

  <section class="card card--front" aria-label="Business card front">
    <svg class="front-art" viewBox="0 0 800 457" preserveAspectRatio="none" aria-hidden="true">
      <defs>
        <linearGradient id="blueFace" x1="0" y1="0" x2="1" y2="1">
          <stop offset="0" stop-color="#6a86dc"/>
          <stop offset="1" stop-color="#3a50b8"/>
        </linearGradient>
        <linearGradient id="blackFace" x1="0" y1="0" x2="0" y2="1">
          <stop offset="0" stop-color="#1c1c20"/>
          <stop offset="1" stop-color="#0a0a0c"/>
        </linearGradient>
      </defs>
      <rect width="800" height="457" fill="url(#blueFace)"/>
      <path d="M0 140 Q 400 140 560 457 L0 457 Z" fill="url(#blackFace)"/>
      <path d="M0 140 Q 400 140 560 457" fill="none" stroke="#a34bc9" stroke-width="7"/>
    </svg>

    <div class="contact">
      <h1 class="contact__name">Lena Marsh</h1>
      <p class="contact__title">Director</p>
      <div class="contact__line">000 318 4472
        <svg viewBox="0 0 24 24"><path d="M6 3h4l2 5-3 2a12 12 0 0 0 5 5l2-3 5 2v4a2 2 0 0 1-2 2A17 17 0 0 1 4 5a2 2 0 0 1 2-2z" fill="#f3b9cf"/></svg>
      </div>
      <div class="contact__line">444 690 2158
        <svg viewBox="0 0 24 24"><rect x="6" y="2" width="12" height="20" rx="2" fill="none" stroke="#ffffff" stroke-width="2"/></svg>
      </div>
      <div class="contact__line">lena@quartzmail.com
        <svg viewBox="0 0 24 24"><rect x="2" y="5" width="20" height="14" rx="2" fill="#f3b9cf"/><path d="M3 6l9 7 9-7" fill="none" stroke="#3a50b8" stroke-width="2"/></svg>
      </div>
      <div class="contact__address">
        <div class="contact__line">2714 E. Palmer Ave Suite 482B
          <svg viewBox="0 0 24 24"><path d="M12 2a7 7 0 0 0-7 7c0 5 7 13 7 13s7-8 7-13a7 7 0 0 0-7-7z" fill="#f3b9cf"/><circle cx="12" cy="9" r="2.5" fill="#3a50b8"/></svg>
        </div>
        <div class="contact__line">North Las Vegas, Nevada 97415<span class="contact__spacer"></span></div>
      </div>
    </div>

    <div class="brand">
      <span class="brand__dot"></span>
      <span class="brand__name">Quartz<br>Traders</span>
    </div>
  </section>

  <section class="card card--back" aria-label="Business card back">
    <div class="brand">
      <span class="brand__dot"></span>
      <span class="brand__name">Quartz<br>Traders</span>
    </div>
  </section>

</main>
</body>
</html>
```